Bref créative
Business Cards & Satationary for Copperfield Homes
Dallin Marsh
Professional
Copperfield Homes
PO Box 587
KELMORE RISE Q 4390
M: 0417 562 908
info@copperfieldhomes.com.au
www.copperfieldhomes.com.au
NHRA Licence No. 80394. Housing Registry Office of Tasmania No. HR-K61402
Residential Construction
"Builder of Quality not Quantity"
E:info@copperfieldhomes.com.au

```html
<!DOCTYPE html>
<html lang="en">
<head>
<meta charset="utf-8">
<title>Copperfield Homes – Business Card</title>
<link href="https://fonts.googleapis.com/css2?family=Cinzel:wght@400;600&family=Open+Sans:wght@400;600&display=swap" rel="stylesheet">
<style>
  :root {
    --orange: #e4522a;
    --orange-deep: #c9401d;
    --white: #ffffff;
    --grey: #a9a9a9;
    --grey-light: #d9d9d9;
    --backdrop: #eeeeee;
    --ink: #4a4a4a;
  }
  * { margin: 0; padding: 0; box-sizing: border-box; }
  html, body { width: 1200px; height: 1009px; overflow: hidden; }
  body {
    background: var(--backdrop);
    font-family: "Open Sans", Arial, sans-serif;
    display: flex;
    flex-direction: column;
    align-items: center;
    justify-content: center;
    gap: 50px;
  }
  .card {
    position: relative;
    width: 700px;
    height: 428px;
    border-radius: 22px;
    overflow: hidden;
    box-shadow: 0 6px 18px rgba(0,0,0,.18);
  }
  .card-front { background: var(--white); }
  .card-back { background: linear-gradient(135deg, var(--orange) 0%, var(--orange-deep) 100%); }
  .card-shapes { position: absolute; inset: 0; }

  .brand {
    position: absolute;
    display: flex;
    align-items: center;
    gap: 16px;
    font-family: "Cinzel", Georgia, serif;
    font-weight: 600;
  }
  .brand-square { width: 52px; height: 52px; }
  .front-brand { top: 96px; left: 230px; color: var(--ink); font-size: 38px; }
  .front-brand .brand-square { background: var(--orange); }
  .brand-tagline {
    position: absolute; top: 158px; left: 298px;
    font-size: 13px; letter-spacing: 8px; color: var(--grey); text-transform: uppercase;
  }

  .contact-list {
    position: absolute; left: 28px; top: 258px;
    list-style: none; color: var(--white); font-size: 13px; line-height: 24px;
  }
  .contact-list li { display: flex; align-items: center; gap: 9px; }
  .contact-icon { width: 13px; height: 13px; flex: none; }
  .card-name {
    position: absolute; right: 30px; bottom: 14px;
    color: var(--white); font-size: 14px; font-weight: 600;
  }

  .back-brand { top: 150px; left: 50%; transform: translateX(-50%); color: var(--white); font-size: 36px; white-space: nowrap; }
  .back-brand .brand-square { background: var(--white); }
  .back-url {
    position: absolute; top: 248px; width: 100%; text-align: center;
    color: var(--white); font-size: 14px; letter-spacing: 4px;
  }
</style>
</head>
<body>

<section class="card card-front">
  <svg class="card-shapes" viewBox="0 0 700 428" aria-hidden="true">
    <path d="M0,150 C230,175 450,270 700,352 L700,380 C450,300 230,205 0,182 Z" fill="var(--grey-light)"/>
    <path d="M0,168 C230,195 450,290 700,372 L700,386 C450,306 230,212 0,186 Z" fill="var(--grey)"/>
    <path d="M0,190 C230,215 450,310 700,392 L700,428 L0,428 Z" fill="var(--orange)"/>
  </svg>

  <div class="brand front-brand">
    <span class="brand-square"></span>
    <span class="brand-name">Copperfield Homes</span>
  </div>
  <div class="brand-tagline">Residential Construction</div>

  <ul class="contact-list">
    <li>
      <svg class="contact-icon" viewBox="0 0 12 12"><path d="M6 0a4 4 0 0 0-4 4c0 3 4 8 4 8s4-5 4-8a4 4 0 0 0-4-4zm0 5.5a1.5 1.5 0 1 1 0-3 1.5 1.5 0 0 1 0 3z" fill="#fff"/></svg>
      PO Box 587, KELMORE RISE Q 4390
    </li>
    <li>
      <svg class="contact-icon" viewBox="0 0 12 12"><rect x="3" y="0.5" width="6" height="11" rx="1.2" fill="none" stroke="#fff" stroke-width="1.2"/><circle cx="6" cy="9.6" r=".7" fill="#fff"/></svg>
      M: 0417 562 908
    </li>
    <li>
      <svg class="contact-icon" viewBox="0 0 12 12"><rect x=".6" y="2" width="10.8" height="8" rx="1" fill="none" stroke="#fff" stroke-width="1.2"/><path d="M1 2.6l5 4 5-4" fill="none" stroke="#fff" stroke-width="1.2"/></svg>
      info@copperfieldhomes.com.au
    </li>
    <li>
      <svg class="contact-icon" viewBox="0 0 12 12"><circle cx="6" cy="6" r="5.3" fill="none" stroke="#fff" stroke-width="1.2"/><path d="M.8 6h10.4M6 .7c-3 3-3 7.6 0 10.6M6 .7c3 3 3 7.6 0 10.6" fill="none" stroke="#fff" stroke-width="1"/></svg>
      www.copperfieldhomes.com.au
    </li>
  </ul>

  <p class="card-name">Dallin Marsh</p>
</section>

<section class="card card-back">
  <div class="brand back-brand">
    <span class="brand-square"></span>
    <span class="brand-name">Copperfield Homes</span>
  </div>
  <p class="back-url">www.copperfieldhomes.com.au</p>
</section>

</body>
</html>
```